・メインで紹介していただく2つのアクティビティーの情報は
以下のHPアドレスにございます。
https://kurumi-lodge.example.jp/wp/activities/星あかりの小径/
https://kurumi-lodge.example.jp/wp/activities/ムーンライトトレック/

・写真素材はグーグルのマイドライブ↓に格納いたしました
https://files.example.net/open?id=8XqPzLmTr2WvNc4Ka7bYdE1hJsG9uFoRt

・写真素材についてはトリミングも含め自由にお使いいただけます。デザインによっては数枚省いていただいても結構です。
~写真の説明~
1「山岳学舎を取り巻く山々」×2のどちらか :山岳学舎施設が山の中にあるというイメージを前面に押し出して頂きたい。
2「山岳学舎紹介・・・・」の写真は施設情報のところで小さくお使いください
そのなかでも「スカイランタン」と「スノースライダー」は こんなこともや
っているよ!程度の小さな丸切り抜きで添えてもらえれば結構です。

・納期期限:10月4日厳守でお願いします。作成過程で、連絡を取りながら作成していただける方を優先させていただきたいと存じます。
【星あかりの小径】
■催行期間 2019年 12月 14日(土)~2020年 4月5日(日) 一日3回
■料  金 小学生以上2,000円(スノーシューレンタル料込)/ 未就学児童 550円  ★山岳学舎ご宿泊者は1,000円 / 未就学児童 無料!!
【ムーンライトトレック】
■催行期間 2019年12月28日~2020年1月5日毎日
2,019年1月11日~3月22日までの土日祝祭日のみ  一日2回
■料  金 小学生以上3,800円(スノーシューレンタル料込)

<施設情報>くるみ原山岳学舎
宿泊 お一人様10,900円~(1泊2食)」〒503-2417 岐阜県大野郡白川村桐ヶ平518
05769-3-4072 https://kurumi-lodge.example.jp/ info@kurumi-gakusha.example

```html
<!DOCTYPE html>
<html lang="ja">
<head>
<meta charset="utf-8">
<title>雪の森を歩こう!</title>
<link href="https://fonts.googleapis.com/css2?family=Noto+Sans+JP:wght@400;700;900&family=Yuji+Syuku&display=swap" rel="stylesheet">
<style>
:root{
  --sky:#9cc6e6;
  --snow:#f4f8fb;
  --forest:#5d7388;
  --blue:#1f78c1;
  --blue-dark:#15548a;
  --pale:#e3f0fa;
  --green:#3a9a3a;
  --red:#e2231a;
  --ink:#222;
  --white:#fff;
}
*{margin:0;padding:0;box-sizing:border-box}
html,body{width:846px;height:1200px;overflow:hidden;background:var(--white)}
body{font-family:"Noto Sans JP",sans-serif;color:var(--ink)}
.poster{position:relative;width:846px;height:1200px;overflow:hidden}
.scene{position:absolute;left:0;top:0;width:846px;height:846px;
  background:linear-gradient(180deg,#7fb3dc 0%,#b9d7ee 22%,#eef4f9 40%,#a9b7c4 55%,#dfe8f0 72%,#f3f7fa 100%)}
.title{position:absolute;right:28px;top:40px;font-family:"Yuji Syuku",serif;color:var(--white);
  text-shadow:0 0 6px rgba(30,50,80,.7),2px 3px 0 rgba(40,60,90,.5);line-height:1.05;text-align:right;font-weight:400}
.title .l1{display:block;font-size:128px;letter-spacing:4px}
.title .l2{display:block;font-size:104px;margin-right:10px}
.card{position:absolute;top:316px;width:324px;height:520px;background:var(--pale);border-radius:6px;overflow:hidden;
  box-shadow:0 2px 6px rgba(0,0,0,.25)}
.card.walk{left:99px}
.card.hike{left:441px}
.card-head{height:38px;background:var(--white);border:3px solid var(--green);border-bottom:none;border-radius:6px 6px 0 0;
  color:var(--green);font-weight:900;font-size:20px;text-align:center;line-height:34px}
.card-photo{height:206px;background:linear-gradient(160deg,#cfdeea,#8fa6ba 60%,#e9f0f6)}
.card-info{padding:10px 16px;font-size:12.5px;line-height:1.5}
.pill{display:block;width:120px;margin:2px auto 4px;background:var(--blue);color:var(--white);border-radius:12px;
  text-align:center;font-weight:700;font-size:13px;line-height:22px}
.dates{text-align:center;font-weight:700;font-size:14px}
.red{color:var(--red);font-weight:700}
.note{font-size:10.5px;line-height:1.5;margin-top:6px;color:#333}
.strip{position:absolute;top:854px;left:18px;display:flex;gap:6px;align-items:center}
.strip .ph{width:84px;height:80px;background:linear-gradient(150deg,#c9d6e2,#8197ab)}
.strip .dot{width:70px;height:70px;border-radius:50%;background:linear-gradient(150deg,#f3c98a,#4a5a7a)}
.stay{position:absolute;left:470px;top:852px;width:360px}
.stay-lead{color:var(--blue);font-weight:900;font-size:22px}
.stay-price{margin-top:6px;background:var(--blue);color:var(--white);font-weight:700;font-size:21px;padding:4px 10px;border-radius:4px;white-space:nowrap}
.stay-price small{font-size:12px}
.org{position:absolute;left:22px;top:990px;width:410px}
.org-name{display:flex;align-items:center;gap:10px;font-weight:900;font-size:24px;color:var(--blue-dark)}
.org-name i{width:22px;height:22px;background:var(--blue-dark);display:inline-block}
.org-addr{margin-top:14px;font-size:13px}
.contact{position:absolute;left:446px;top:958px;width:384px;height:222px;border:2px solid var(--blue);border-radius:8px;padding:0 14px 12px}
.contact-head{margin:0 -14px 14px;background:var(--blue);color:var(--white);text-align:center;font-size:14px;font-weight:700;line-height:28px}
.row{display:flex;align-items:center;gap:10px;color:var(--blue-dark);font-weight:900;margin:12px 0;white-space:nowrap}
.row svg{flex:none}
.row.url{font-size:18px}
.row.tel{font-size:34px}
.row.mail{font-size:17px}
</style>
</head>
<body>
<div class="poster">
  <div class="scene" role="img" aria-label="雪に覆われた山々と森に囲まれた山岳学舎の冬景色の写真"></div>
  <h1 class="title"><span class="l1">雪の森</span><span class="l2">を歩こう!</span></h1>

  <section class="card walk">
    <h2 class="card-head">星あかりの小径</h2>
    <div class="card-photo" role="img" aria-label="雪の森を散歩する参加者の写真"></div>
    <div class="card-info">
      <span class="pill">催行期間</span>
      <p class="dates">2019/12/14(土)～2020/4/5(日)</p>
      <p class="dates">※1日3回</p>
      <span class="pill">料 金</span>
      <p>■小学生以上 2,000円（スノーシューレンタル料込）</p>
      <p>■未就学児童 550円</p>
      <p class="red">●山岳学舎ご宿泊者様は1,000円</p>
      <p class="red">●未就学児童 無料!</p>
      <p class="note">雪に覆われた静かな森をスノーシューでゆっくり歩きます。動物の足跡や冬芽を探しながら、冬の森の自然をガイドと一緒に楽しみましょう。初めての方でも安心です。</p>
    </div>
  </section>

  <section class="card hike">
    <h2 class="card-head">ムーンライトトレック</h2>
    <div class="card-photo" role="img" aria-label="スノーシューで雪山を歩く参加者の写真"></div>
    <div class="card-info">
      <span class="pill">催行期間</span>
      <p class="dates">2019/12/28(土)～2020/1/5(日)</p>
      <p class="dates">※毎日</p>
      <p class="red" style="text-align:center">2020/1/11(土)～3/22(日)までの<br>土日祝祭日のみ1日2回</p>
      <span class="pill">料 金</span>
      <p>■小学生以上 3,800円（スノーシューレンタル料込）</p>
      <p class="note">山の斜面や尾根を歩き、白く輝く景色を眺めます。雪の上でのおやつ休憩もお楽しみに。体力に合わせてコースを選び、冬山の魅力を味わいましょう。</p>
    </div>
  </section>

  <div class="strip">
    <div class="ph" role="img" aria-label="山岳学舎の外観写真"></div>
    <div class="ph" role="img" aria-label="山岳学舎の客室写真"></div>
    <div class="dot" role="img" aria-label="スカイランタンの写真"></div>
    <div class="dot" role="img" aria-label="スノースライダーの写真"></div>
  </div>

  <div class="stay">
    <p class="stay-lead">ご宿泊はくるみ原山岳学舎で!</p>
    <p class="stay-price">宿泊料金10,900円～<small>（お一人様/1泊2食付）</small></p>
  </div>

  <div class="org">
    <p class="org-name"><i></i>くるみ原山岳学舎</p>
    <p class="org-addr">〒503-2417 岐阜県大野郡白川村桐ヶ平518</p>
  </div>

  <div class="contact">
    <p class="contact-head">お問い合わせ・詳しい情報はこちらから</p>
    <p class="row url"><svg width="24" height="24" viewBox="0 0 26 26"><circle cx="13" cy="13" r="11" fill="none" stroke="currentColor" stroke-width="2"/><ellipse cx="13" cy="13" rx="5" ry="11" fill="none" stroke="currentColor" stroke-width="2"/><line x1="2" y1="13" x2="24" y2="13" stroke="currentColor" stroke-width="2"/></svg>https://kurumi-lodge.example.jp</p>
    <p class="row tel"><svg width="30" height="30" viewBox="0 0 24 24"><path fill="currentColor" d="M6.6 10.8a15 15 0 0 0 6.6 6.6l2.2-2.2a1 1 0 0 1 1-.25 11.4 11.4 0 0 0 3.6.57 1 1 0 0 1 1 1V20a1 1 0 0 1-1 1A17 17 0 0 1 3 4a1 1 0 0 1 1-1h3.5a1 1 0 0 1 1 1c0 1.25.2 2.45.57 3.57a1 1 0 0 1-.25 1z"/></svg>05769-3-4072</p>
    <p class="row mail"><svg width="26" height="20" viewBox="0 0 28 22"><rect x="1" y="1" width="26" height="20" rx="2" fill="none" stroke="currentColor" stroke-width="2"/><path d="M2 3l12 9 12-9" fill="none" stroke="currentColor" stroke-width="2"/></svg>info@kurumi-gakusha.example</p>
  </div>
</div>
</body>
</html>
```